New Web Design Project shop crate

We are about to start a new furniture selling website and it will be based on shop crate . we mainly need two pages designing landing page & item page. so come up with your unique ideas and designs . Please make sure the design needs to be unique . no templates and themes . Will make the selected designer even happier if your design is selected. So basically over all it is going to be the new theme for our shop crate base eCommerce website .we will appreciate if its responsive with some unique features .
SO as per request of designers about more brief about the project = WE ONLY NEED A RESPONSIVE THEME FOR OUR SHOP CRATE BASE eCommerce WebSite . Mainly item page & product page needs a good unique design. Lighter, speed load, compatible with all browsers and responsive will be appreciated . To Get an idea check on sofahaven .co .uk website or chairmeadow etc.
more projects coming soon .

Target Market(s)

Our audience will be furniture buying customers .

Industry/Entity Type

Furniture

Requirements
Must have
• to get some sort of idea have a look at sofahaven .co uk`s website`s listing page and landing page .
Nice to have
• responsive, easy to customize, full theme .

```html
<!DOCTYPE html>
<html lang="en">
<head>
<meta charset="utf-8">
<title>Timber Nook – Product</title>
<link href="https://fonts.googleapis.com/css2?family=Lato:wght@400;700&display=swap" rel="stylesheet">
<style>
:root{
  --pink:#d91e4f;
  --teal:#1a93a6;
  --green:#7fb03a;
  --orange:#f49a1c;
  --ink:#333;
  --soft:#666;
  --line:#d6d6d6;
  --dark:#2b2b2b;
}
*{box-sizing:border-box;margin:0;padding:0}
html,body{width:790px;height:1200px;overflow:hidden;background:#fff;font-family:'Lato',sans-serif;color:var(--ink)}
.page{position:relative;width:790px;height:1200px}
.abs{position:absolute}
.icon{display:inline-block;vertical-align:middle}
.auth{left:574px;top:0;width:130px;height:24px;display:flex}
.auth span{flex:1;background:var(--green);color:#fff;font-size:9px;display:flex;align-items:center;justify-content:center;gap:4px}
.auth span+span{border-left:1px solid #6b9a2e}
.brand{left:86px;top:14px;display:flex;align-items:center;gap:8px}
.brand-mark{width:34px;height:34px;background:var(--pink);border-radius:6px}
.brand-name{font-size:28px;font-weight:700;color:var(--ink);line-height:1}
.account{top:40px;right:86px;display:flex;gap:14px;font-size:9px;color:var(--soft)}
.search{left:405px;top:66px;width:187px;height:24px;border:1px solid var(--line);font-size:8px;color:#888;padding:7px 8px}
.search svg{position:absolute;right:6px;top:6px}
.cart{left:602px;top:66px;width:102px;height:24px;border:1px solid var(--line);font-size:9px;font-weight:700;display:flex;align-items:center;justify-content:center;gap:4px}
.nav{left:0;top:102px;width:790px;height:31px;background:var(--pink);border-top:2px solid #b3173f}
.nav ul{list-style:none;display:flex;position:absolute;left:86px;top:0;height:29px}
.nav li{color:#fff;font-size:10px;display:flex;align-items:center;padding:0 19px;border-right:1px solid #e65f82;height:13px;margin-top:8px}
.nav li.active{background:var(--teal);height:29px;margin-top:0;padding:0 21px;border:none}
.nav li:last-child{border:none}
.crumbs{left:86px;top:147px;font-size:7.5px}
.title{left:86px;top:169px;width:618px;font-size:15px;font-weight:400;padding-bottom:6px;border-bottom:1px solid var(--line)}
.photo{left:86px;top:206px;width:180px;height:166px;border:1px solid var(--line);padding:28px 12px}
.photo div,.thumb div{width:100%;height:100%;background:linear-gradient(180deg,#f7f4f1 0%,#5a4032 45%,#4a3426 75%,#f3efeb 100%)}
.thumb{top:378px;width:52px;height:46px;border:1px solid var(--line);padding:6px}
.card .img{width:100%;height:90px;background:linear-gradient(#f6f3f0,#e9e3de)}
.stars{left:284px;top:205px;display:flex;gap:1px;align-items:center;font-size:8px}
.stars span{margin-left:6px}
.price{left:285px;top:236px;font-size:14px;color:#444;padding-right:10px;border-right:1px solid var(--line);height:26px}
.delivery{left:357px;top:233px;font-size:8px;line-height:15px}
.qty{left:284px;top:277px;width:174px;height:33px;background:#eee;display:flex;align-items:center;gap:6px;padding-left:7px;font-size:8.5px}
.qty .box{width:20px;height:18px;border:1px solid #ccc;background:#fff;display:flex;align-items:center;justify-content:center}
.btn{background:var(--teal);color:#fff;font-size:8.5px;font-weight:700;display:inline-flex;align-items:center;gap:6px;padding:0 7px;height:20px}
.desc-h{left:284px;top:324px;width:420px;font-size:11.5px;font-weight:400;padding-bottom:4px;border-bottom:1px solid var(--line)}
.desc{left:284px;top:346px;width:420px;font-size:8.3px;line-height:13.9px;color:#555}
.tabs{left:284px;top:450px;display:flex;gap:6px}
.tabs span{height:24px;border:1px solid var(--line);border-bottom:none;font-size:8.5px;font-weight:700;padding:0 7px;display:flex;align-items:center;color:#555}
.tabs span.on{background:var(--teal);color:#fff;border-color:var(--teal)}
.spec{left:284px;top:474px;width:420px;border:1px solid var(--line);border-collapse:collapse;font-size:8px}
.spec td{height:24.7px;border-bottom:1px solid var(--line);padding-left:13px}
.spec td:first-child{font-weight:700;width:178px}
.related-h{left:86px;top:746px;width:618px;height:24px;background:repeating-linear-gradient(135deg,#e3e3e3 0 1px,#fff 1px 3px) bottom/100% 5px no-repeat}
.related-h span{display:inline-block;height:24px;background:var(--orange);color:#fff;font-size:12.5px;padding:5px 18px 0 9px;clip-path:polygon(0 0,93% 0,100% 100%,0 100%)}
.card{top:782px;width:146px;height:188px;border:1px solid var(--line);padding:10px 8px 0}
.card .p{font-size:11px;margin:12px 0 0 2px;color:#444}
.card .n{font-size:9.3px;font-weight:700;margin-top:10px}
.card .btn{margin-top:10px}
.rule{left:86px;top:982px;width:618px;height:5px;background:repeating-linear-gradient(135deg,#e3e3e3 0 1px,#fff 1px 3px)}
.partners{left:86px;top:1010px;width:618px;display:flex;justify-content:space-between;font-size:11.5px;font-weight:700;color:#333}
.footer{left:0;top:1049px;width:790px;height:126px;background:var(--dark)}
.col{top:14px;color:#ddd}
.col h4{font-size:12px;font-weight:400;color:#eee;padding-bottom:6px;border-bottom:1px solid #444;margin-bottom:8px}
.col li{list-style:none;font-size:8.5px;line-height:19.5px}
.col li::before{content:"›";margin-right:5px}
.col p{font-size:8.5px;line-height:13px}
.email{width:126px;height:18px;background:#fff;color:#888;font-size:7px;padding:4px 6px;margin-top:8px}
.sub{display:inline-block;background:#aaa;color:#222;font-size:8.5px;font-weight:700;padding:3px 7px;margin-top:7px}
.social div{display:flex;align-items:center;gap:7px;font-size:8.5px;height:23px}
.social i{width:15px;height:15px;background:#eee;display:inline-block}
.bottom{left:0;top:1175px;width:790px;height:25px;background:var(--pink);color:#fff;font-size:8.5px;padding:7px 0 0 88px}
.cards{position:absolute;right:92px;top:5px;display:flex;gap:2px}
.cards span{width:25px;height:15px;background:#fff;color:#333;font-size:5.5px;display:flex;align-items:center;justify-content:center}
</style>
</head>
<body>
<svg width="0" height="0" style="position:absolute">
  <symbol id="basket" viewBox="0 0 12 10"><path d="M1 4h10l-1.3 5H2.3z" fill="currentColor"/><path d="M3 4l3-3 3 3" fill="none" stroke="currentColor" stroke-width="1"/></symbol>
</svg>
<div class="page">
  <div class="abs auth"><span>Login</span><span>Register</span></div>
  <div class="abs brand"><span class="brand-mark"></span><span class="brand-name">Timber Nook</span></div>
  <div class="abs account"><span>My Account</span><span>My Wishlist</span><span>Checkout</span></div>
  <div class="abs search">Search
    <svg width="10" height="10" viewBox="0 0 10 10"><circle cx="4" cy="4" r="3" fill="none" stroke="#666" stroke-width="1.3"/><line x1="6.3" y1="6.3" x2="9" y2="9" stroke="#666" stroke-width="1.3"/></svg></div>
  <div class="abs cart"><svg class="icon" width="12" height="10"><use href="#basket"/></svg> Shopping Cart ⌄</div>

  <nav class="abs nav"><ul>
    <li class="active">HOME</li><li>BEDROOM</li><li>LIVING ROOM</li><li>DINING ROOM</li><li>KIDS ROOMS</li><li>BRANDS</li><li>SALE</li>
  </ul></nav>

  <div class="abs crumbs">Home &nbsp;» &nbsp;Categories &nbsp;» &nbsp;Living Room</div>
  <h1 class="abs title">Neque porro quisquam est qui dolorem ipsum quia dolor sit ametx</h1>

  <div class="abs photo"><div role="img" aria-label="Dark brown sectional sofa with ottoman"></div></div>
  <div class="abs thumb" style="left:93px"><div role="img" aria-label="Sofa view one"></div></div>
  <div class="abs thumb" style="left:150px"><div role="img" aria-label="Sofa view two"></div></div>
  <div class="abs thumb" style="left:208px"><div role="img" aria-label="Sofa view three"></div></div>

  <div class="abs stars">
    <svg width="70" height="12" viewBox="0 0 70 12"><g fill="#f49a1c">
      <polygon id="s" points="6,0 7.6,4.2 12,4.4 8.5,7.1 9.7,11.5 6,9 2.3,11.5 3.5,7.1 0,4.4 4.4,4.2"/>
      <use href="#s" x="14"/><use href="#s" x="28"/><use href="#s" x="42"/><use href="#s" x="56"/></g></svg>
    <span>3 Review(s) &nbsp; Add Your Review</span></div>
  <div class="abs price">$100.95</div>
  <div class="abs delivery"><b>Delivery:</b> within 4-8 Working days<br><b>Delivery price:</b> $14.00 or FREE on orders over $300 (subject to location)</div>
  <div class="abs qty">Quantity <span class="box">1</span><span class="btn" style="margin-left:6px;height:21px"><svg width="12" height="10"><use href="#basket"/></svg>ADD TO CART</span></div>

  <h2 class="abs desc-h">Description</h2>
  <p class="abs desc">Sed ut perspiciatis unde omnis iste natus error sit voluptatem accusantium doloremque laudantium, totn rem aperiam, eaque ipsa quae ab illo inventore veritatis et quasi architecto beatae vitae dicta sunt explicabn Nemo enim ip voluptatem quia voluptas sit aspernatur aut odit aut fugit, consequuntur magni dolores eos in ratione voluptatem sequi nesciunt. Lorem ipsum dolor sit amet, consectetur adipisicing elit, sed do eiusmo incididunt ut labore et dolore magna aliqua. Ut enim ad minim veniam, quis nostrud exercitation ullamco laboris aliquip ex ea commodo consequat. Duis aute irure dolor in reprehenderit.</p>

  <div class="abs tabs"><span class="on">Specification</span><span>Reviews</span><span>Add Reviews</span></div>
  <table class="abs spec">
    <tr><td>Product Code</td><td>Lorem ipsum dolor sit amet, consectetur</td></tr>
    <tr><td>Height</td><td>1905mm</td></tr>
    <tr><td>Width</td><td>1499mm</td></tr>
    <tr><td>Depth</td><td>584mm</td></tr>
    <tr><td>Weight</td><td>83kg</td></tr>
    <tr><td>Material</td><td>Pine</td></tr>
    <tr><td>Finish</td><td>Waxed</td></tr>
    <tr><td>Assembled</td><td>Easy Home Assembly Required</td></tr>
    <tr><td>Doors</td><td>3</td></tr>
    <tr><td>Wardrobes size</td><td>3 Door/Triple</td></tr>
  </table>

  <div class="abs related-h"><span>RELATED PRODUCTS</span></div>
  <div class="abs card" style="left:86px"><div class="img" role="img" aria-label="Upholstered wooden storage bed"></div><div class="p">$199.00</div><div class="n">Lorem ipsum dolor sit amet</div><span class="btn"><svg width="12" height="10"><use href="#basket"/></svg>ADD TO CART</span></div>
  <div class="abs card" style="left:244px"><div class="img" role="img" aria-label="Carved wooden dining chair"></div><div class="p">$100.95</div><div class="n">Lorem ipsum dolor sit amet</div><span class="btn"><svg width="12" height="10"><use href="#basket"/></svg>ADD TO CART</span></div>
  <div class="abs card" style="left:401px"><div class="img" role="img" aria-label="Brown sectional sofa with ottoman"></div><div class="p">$100.95</div><div class="n">Lorem ipsum dolor sit amet</div><span class="btn"><svg width="12" height="10"><use href="#basket"/></svg>ADD TO CART</span></div>
  <div class="abs card" style="left:558px"><div class="img" role="img" aria-label="Dark wood dining table with chairs"></div><div class="p">$100.95</div><div class="n">Lorem ipsum dolor sit amet</div><span class="btn"><svg width="12" height="10"><use href="#basket"/></svg>ADD TO CART</span></div>

  <div class="abs rule"></div>
  <div class="abs partners"><span>Corvane</span><span>Archlow</span><span>nodra</span><span>Palewick</span><span>Tarvell</span><span>Genova</span><span>Rosmere</span><span>Fernhollow</span></div>

  <footer class="abs footer">
    <div class="abs col" style="left:94px;width:92px"><h4>Products</h4><ul><li>Bedroom</li><li>Living Room</li><li>Dining Room</li><li>Kids Rooms</li></ul></div>
    <div class="abs col" style="left:205px;width:86px"><h4>Information</h4><ul><li>Home</li><li>About Us</li><li>Blog</li><li>Contact us</li></ul></div>
    <div class="abs col" style="left:329px;width:86px"><h4>Your Account</h4><ul><li>Order Status</li><li>My Wishlist</li><li>Order History</li><li>Newsletter</li></ul></div>
    <div class="abs col" style="left:452px;width:126px"><h4>Newsletter Sign Up</h4><p>Lorem ipsudolor sit ec adipiscing elitsite amet</p><div class="email">Email Address</div><span class="sub">SUBSCRIBE</span></div>
    <div class="abs col social" style="left:620px;width:84px"><h4>Follow us</h4><div><i></i>Friendspace</div><div><i></i>Chirper</div><div><i></i>Circlet</div></div>
  </footer>
  <div class="abs bottom">© Copyright 2014 Timber Nook. All Right Reserved
    <div class="cards"><span>Payra</span><span>Kestra</span><span>Orbit</span><span>Nimbus</span><span>Tessel</span></div></div>
</div>
</body>
</html>
```